Velmora CBD Tincture packaging design

We are seeking a designer to create the label that will be printed on cardboard box packaging, which will carry our CBD tincture. We envision the box being white to resemble a clean look that stands out on shelves. Our logo (attached) uses shades of yellows and greens in the form of a fluid drop resembling half plant and half plant extract. The packaging will show that we only use clean (TRUNK certified) hemp extract thats been extracted using the cleanest method of extraction; supercritical CO2. Our tincture uses a fractionated coconut oil to improve absorption for the consumer, increasing onset time and providing essential omega fatty acids. We take pride in our use of a clean product with a clean extraction. The tincture bottle itself holds 30ml of liquid and is a clear glass bottle. The cap for the tincture bottle is white and has a graduated glass stem that shows the measurements for how much liquid it holds (picture attached). We have not yet done the label that will stick on the tincture, but i image it will be a frosted white label with the Velmora logo and a few words describing the product. This project is for the cardboard box that will hold each individual tincture bottle.

BOX DIMENSIONS: 1.31" x 1.31" x 4.13" (LxWxH)

We will be releasing a new product (cbd capsules) in April, and we will reach out to the designer of this product as first option to create the design for the capsule packaging.

Target Market(s)

convenience stores, medical marijuana dispensaries, health stores

Font styles to use
Serif

Colors
ffffff
fbed22
ffc214
ffcf3e
acd136
9bcb3c

Requirements
Must have
• -Velmora company logo
-Made with full spectrum supercritical CO2 Hemp Extract
-Made from TRUNK certified clean hemp
-Declaration of ingredients (fractionated coconut oil, CBD hemp extract)
-1200mg CBD Tincture
-Nt. Wt. 1FL OZ (30ml)
-These statements have not been evaluated by the Food and Drug Administration. FDA has not evaluated this product for safety or efficacy. This product is not intended to diagnose, treat, cure or prevent any disease.
-DO NOT REFRIGERATE. Keep at room temperature to preserve freshness. Store away from humidity, heat, and light. Warning: If pregnant, nursing or taking prescription drugs, consult your physician prior to use. Keep out of reach of children.
-Manufactured by Velmora CBD Co. 58 Quarry Bend Rd. Larkfield, VT 05019
-Batch ID:___________
-Expiration Date:____________
-Good Manufacturing Practice (GMP) Logo
-TRUNK logo
Nice to have
• -Contains omega 3, 6 and essential fatty acids
-Graduated dropper for precise dosing
-40mg of CBD per dropper!
-Made in the USA
-No Pesticides
-No Solvents
-No Heavy Metals
-CO2 Extraction
-3rd Party Lab Tested

```html
<!DOCTYPE html>
<html lang="en">
<head>
<meta charset="utf-8">
<title>Velmora CBD Tincture – Box Panels</title>
<link rel="stylesheet" href="https://fonts.googleapis.com/css2?family=Tinos:wght@400;700&display=swap">
<style>
  :root {
    --bg: #d6d6d6;
    --paper: #ffffff;
    --ink: #333333;
    --green: #2e9b32;
    --leaf: #9bcb3c;
    --tick: #e8643c;
    --fold: #e4e4e4;
  }
  * { box-sizing: border-box; margin: 0; padding: 0; }
  html, body { width: 1200px; height: 1200px; overflow: hidden; }
  body {
    background: var(--bg);
    font-family: "Tinos", "Times New Roman", serif;
    color: var(--green);
  }
  .dieline {
    position: absolute;
    left: 60px; top: 170px;
    display: flex;
    width: 1080px; height: 860px;
    background: var(--paper);
    box-shadow: 0 2px 10px rgba(0,0,0,.12);
  }
  .panel {
    position: relative;
    width: 270px; height: 100%;
    padding: 50px 24px 36px;
    display: flex; flex-direction: column; align-items: center;
    border-right: 1px solid var(--fold);
  }
  .panel:last-child { border-right: 0; }

  .brand { display: flex; flex-direction: column; align-items: center; gap: 14px; }
  .brand-dot { width: 46px; height: 46px; border-radius: 50%; background: var(--leaf); }
  .brand-name { font-size: 54px; font-weight: 400; color: var(--ink); line-height: 1; letter-spacing: -1px; }
  .brand.small .brand-dot { width: 38px; height: 38px; }
  .brand.small .brand-name { font-size: 44px; }

  .notice { width: 100%; border: 1.5px solid var(--green); padding: 10px 8px 8px; margin-top: 44px; position: relative; }
  .notice-tab {
    position: absolute; top: -10px; left: -1.5px;
    background: var(--paper); border: 1.5px solid var(--green);
    font-size: 10px; padding: 1px 4px; text-transform: uppercase;
  }
  .notice p, .fine { font-size: 14px; line-height: 1.55; }
  .fine { margin-top: auto; text-align: justify; }

  .product-title { margin-top: 150px; font-size: 38px; font-weight: 700; line-height: 1.25; text-align: left; align-self: flex-start; padding-left: 6px; white-space: nowrap; }
  .title-dot { display: inline-block; width: 18px; height: 18px; border-radius: 50%; background: var(--green); margin-left: 6px; vertical-align: middle; }
  .strength { margin-top: 170px; font-size: 20px; text-align: center; line-height: 1.4; }
  .origin { margin-top: auto; font-size: 18px; font-weight: 700; }

  .features { list-style: none; margin-top: 60px; width: 100%; }
  .features li { display: flex; gap: 8px; font-size: 18px; line-height: 1.35; margin-bottom: 8px; }
  .features svg { flex: none; margin-top: 2px; }
  .maker { margin-top: 40px; font-size: 17px; line-height: 1.35; align-self: flex-start; }
  .record { margin-top: auto; align-self: flex-start; font-size: 17px; line-height: 2; }
  .record span { display: inline-block; width: 100px; border-bottom: 1px solid var(--green); }

  .claim { margin-top: 56px; font-size: 17px; text-align: center; line-height: 1.4; }
  .seal { width: 120px; height: 120px; border-radius: 50%; margin-top: 40px; }
  .seal.ring { border: 10px solid var(--green); opacity: .85; }
  .ingredients { margin-top: 40px; font-size: 17px; text-align: center; line-height: 1.4; }
</style>
</head>
<body>
<main class="dieline">

  <section class="panel panel-care">
    <div class="brand small"><span class="brand-dot"></span><span class="brand-name">Velmora</span></div>
    <div class="notice">
      <span class="notice-tab">Do not refrigerate</span>
      <p>Keep at room temperature to preserve freshness. Store away from humidity, heat, and light.</p>
    </div>
    <div class="notice">
      <span class="notice-tab">Warning</span>
      <p>If pregnant, nursing or taking prescription drugs, consult your physician prior to use. Keep out of reach of children.</p>
    </div>
    <p class="fine">These statements have not been evaluated by the Food and Drug Administration. FDA has not evaluated this product for safety or efficacy. This product is not intended to diagnose, treat, cure or prevent any disease.</p>
  </section>

  <section class="panel panel-front">
    <div class="brand"><span class="brand-dot"></span><span class="brand-name">Velmora</span></div>
    <h1 class="product-title">CBD OIL<span class="title-dot"></span><br>TINCTURE</h1>
    <p class="strength">1200mg CBD Tincture<br>Nt. Wt. 1FL OZ (30ml)</p>
    <p class="origin">Made in the USA</p>
  </section>

  <section class="panel panel-back">
    <div class="brand"><span class="brand-dot"></span><span class="brand-name">Velmora</span></div>
    <ul class="features">
      <li><svg width="18" height="18" viewBox="0 0 18 18"><circle cx="8" cy="10" r="7" fill="none" stroke="var(--tick)" stroke-width="1.6"/><path d="M4 9l4 4 8-11" fill="none" stroke="var(--tick)" stroke-width="2.2"/></svg>Contains omega 3, 6 and essential fatty acids.</li>
      <li><svg width="18" height="18" viewBox="0 0 18 18"><circle cx="8" cy="10" r="7" fill="none" stroke="var(--tick)" stroke-width="1.6"/><path d="M4 9l4 4 8-11" fill="none" stroke="var(--tick)" stroke-width="2.2"/></svg>Graduated dropper for precise dosing.</li>
      <li><svg width="18" height="18" viewBox="0 0 18 18"><circle cx="8" cy="10" r="7" fill="none" stroke="var(--tick)" stroke-width="1.6"/><path d="M4 9l4 4 8-11" fill="none" stroke="var(--tick)" stroke-width="2.2"/></svg>CO2 Extraction.</li>
      <li><svg width="18" height="18" viewBox="0 0 18 18"><circle cx="8" cy="10" r="7" fill="none" stroke="var(--tick)" stroke-width="1.6"/><path d="M4 9l4 4 8-11" fill="none" stroke="var(--tick)" stroke-width="2.2"/></svg>3rd Party Lab Tested.</li>
      <li><svg width="18" height="18" viewBox="0 0 18 18"><circle cx="8" cy="10" r="7" fill="none" stroke="var(--tick)" stroke-width="1.6"/><path d="M4 9l4 4 8-11" fill="none" stroke="var(--tick)" stroke-width="2.2"/></svg>40mg of CBD / dropper!</li>
      <li><svg width="18" height="18" viewBox="0 0 18 18"><circle cx="8" cy="10" r="7" fill="none" stroke="var(--tick)" stroke-width="1.6"/><path d="M4 9l4 4 8-11" fill="none" stroke="var(--tick)" stroke-width="2.2"/></svg>No Pesticides.</li>
      <li><svg width="18" height="18" viewBox="0 0 18 18"><circle cx="8" cy="10" r="7" fill="none" stroke="var(--tick)" stroke-width="1.6"/><path d="M4 9l4 4 8-11" fill="none" stroke="var(--tick)" stroke-width="2.2"/></svg>No Solvents.</li>
      <li><svg width="18" height="18" viewBox="0 0 18 18"><circle cx="8" cy="10" r="7" fill="none" stroke="var(--tick)" stroke-width="1.6"/><path d="M4 9l4 4 8-11" fill="none" stroke="var(--tick)" stroke-width="2.2"/></svg>No Heavy Metals.</li>
    </ul>
    <p class="maker">Manufactured by Velmora CBD Co. 58 Quarry Bend Rd. Larkfield, VT 05019</p>
    <p class="record">Batch ID:<span></span><br>Expiration Date:<span></span></p>
  </section>

  <section class="panel panel-certs">
    <div class="brand small"><span class="brand-dot"></span><span class="brand-name">Velmora</span></div>
    <p class="claim">Made with full spectrum supercritical CO2 Hemp Extract</p>
    <div class="seal ring" role="img" aria-label="TRUNK certified clean hemp badge"></div>
    <p class="ingredients">Declaration of ingredients (fractionated coconut oil, CBD hemp extract)</p>
    <div class="seal ring" role="img" aria-label="Good Manufacturing Practice certified badge"></div>
  </section>

</main>
</body>
</html>
```